Webdesign für psychotherapeutische Praxis
Zielgruppe
Psychotherapeutische Praxis für erwachsene Patienten mit psychischen Erkrankungen.
Die Website soll eine solide, vertrauensvolle Information über das therapeutische Angebot bieten sowie alle Informationen zur Erstkontaktaufnahme erhalten.
Aufgabenstellung
Logo füge ich bei. Die Farben, das Design, die Schrift sollen dem Logo entsprechen (Grau, Violett-Pink Töne, moderne Schrift).

```html
<!DOCTYPE html>
<html lang="de">
<head>
<meta charset="utf-8">
<title>Therapieablauf – Praxis Hollmann</title>
<link rel="stylesheet" href="https://fonts.googleapis.com/css2?family=Fira+Sans:wght@300;400;500&display=swap">
<style>
  :root {
    --violet: #7566b3;
    --violet-line: #b9b0da;
    --text: #3f3f42;
    --nav-text: #3a3a3c;
    --band: #6b6a6b;
    --footer: #4f4e50;
    --white: #ffffff;
    --hero-a: #ddd1e3;
    --hero-b: #c9b6bd;
    --hero-c: #b89f88;
  }
  * { margin: 0; padding: 0; box-sizing: border-box; }
  html, body { width: 888px; height: 1200px; overflow: hidden; }
  body {
    position: relative;
    background: var(--white);
    font-family: "Fira Sans", Arial, sans-serif;
    font-weight: 300;
    color: var(--text);
  }
  .site-header { position: absolute; top: 0; left: 0; width: 888px; height: 46px; background: var(--white); }
  .brand { position: absolute; left: 100px; top: 14px; display: flex; align-items: center; gap: 7px;
    font-size: 11px; font-weight: 400; color: var(--violet); }
  .brand-dot { width: 14px; height: 14px; border-radius: 50%; background: var(--violet); }
  .main-nav a { position: absolute; top: 17px; font-size: 11px; font-weight: 400; color: var(--nav-text); text-decoration: none; }
  .hero { position: absolute; top: 46px; left: 0; width: 888px; height: 130px;
    background: linear-gradient(90deg, var(--hero-a) 0%, var(--hero-a) 32%, var(--hero-b) 65%, var(--hero-c) 100%); }
  .quote { position: absolute; top: 197px; left: 0; width: 888px; text-align: center; }
  .quote p { font-size: 15.5px; font-weight: 400; line-height: 18.5px; color: var(--text); }
  .quote cite { display: block; margin-top: 7px; font-style: normal; font-size: 13px; color: var(--violet); }
  .content { position: absolute; top: 286px; left: 119px; width: 602px; }
  .page-title { font-size: 24px; font-weight: 300; color: var(--violet); line-height: 30px; }
  .title-rule { width: 163px; height: 1px; background: var(--violet-line); margin-top: 17px; }
  .intro { margin-top: 27px; font-size: 15px; line-height: 18.5px; }
  .phase-title { font-size: 15px; font-weight: 400; line-height: 18px; }
  .phase p { margin-top: 13px; font-size: 13.4px; line-height: 16.2px; }
  .phase-1 { margin-top: 21px; }
  .phase-2 { margin-top: 30px; }
  .phase-3 { margin-top: 26px; }
  .cta-band { position: absolute; top: 895px; left: 0; width: 888px; height: 104px; background: var(--band); }
  .cta-text { position: absolute; left: 104px; top: 34px; font-size: 21.5px; font-weight: 300; color: var(--white); }
  .cta-button { position: absolute; left: 484px; top: 35px; width: 135px; height: 34px; border: 1.5px solid var(--white);
    color: var(--white); font-size: 15px; font-weight: 400; text-align: center; line-height: 31px; text-decoration: none; }
  .site-footer { position: absolute; top: 999px; left: 0; width: 888px; height: 201px; background: var(--footer); color: var(--white); }
  .footer-col { position: absolute; top: 40px; }
  .footer-col.contact { left: 184px; width: 213px; }
  .footer-col.notes { left: 471px; width: 260px; }
  .footer-heading { font-size: 13px; font-weight: 400; line-height: 16px; display: inline-block; padding-bottom: 4px; border-bottom: 1px solid rgba(255,255,255,.8); }
  .contact .footer-heading { width: 213px; }
  .notes .h-note { width: 87px; }
  .notes .h-phone { width: 162px; }
  .footer-text { font-size: 11.5px; line-height: 14px; margin-top: 7px; }
  .notes .h-phone { margin-top: 14px; }
  .contact-row { display: flex; align-items: flex-start; gap: 8px; font-size: 11.5px; line-height: 14px; }
  .contact-row svg { flex: none; }
  .row-address { margin-top: 13px; }
  .row-phone { margin-top: 10px; }
  .row-mail { margin-top: 13px; }
</style>
</head>
<body>
  <header class="site-header">
    <div class="brand"><span class="brand-dot"></span>Praxis Hollmann</div>
    <nav class="main-nav">
      <a href="#" style="left:295px">Startseite</a>
      <a href="#" style="left:389px">Therapieangebot</a>
      <a href="#" style="left:527px">Therapieablauf</a>
      <a href="#" style="left:650px">Über mich</a>
      <a href="#" style="left:736px">Kontakt</a>
    </nav>
  </header>

  <div class="hero" role="img" aria-label="Blühende Baumzweige vor hellviolettem Himmel"></div>

  <blockquote class="quote">
    <p>„Es ist nicht gesagt, dass es besser wird, wenn es anders wird.<br>Wenn es aber besser werden soll, muss es anders werden.“</p>
    <cite>Marten Hollweg</cite>
  </blockquote>

  <main class="content">
    <h1 class="page-title">Therapieverlauf</h1>
    <div class="title-rule"></div>
    <p class="intro">Der Therapieverlauf lässt sich<br>in 3 Phasen untergliedern:</p>

    <section class="phase phase-1">
      <h2 class="phase-title">1. Sprechstunden und Probatorik</h2>
      <p>Den Anfang einer Psychotherapie bildet zunächst das Erstgespräch. In diesem Gespräch steht das gegenseitige Kennenlernen im Vordergrund. Gemeinsam soll erarbeitet werden, ob eine Indikation für eine ambulante Psychotherapie besteht und inwiefern das Therapieangebot und ihre Therapieziele zueinander passen. Anschließend folgen weitere Sprechstunden und sogenannte probatorische Sitzungen. Ziel dieser Startphase ist die Diagnostik, die Problemanalyse, die biografische Anamnese und die Erstellung eines Therapieplans.</p>
    </section>

    <section class="phase phase-2">
      <h2 class="phase-title">2. Therapie</h2>
      <p>Zum Ende der obengenannten Phase wird ein Therapieantrag nach gemeinsamer Absprache an Ihre Krankenkasse gesendet. Nach dessen Genehmigung startet dann die eigentliche Therapiephase (2 x 12 Sitzungen bei einer Kurzzeit-, 60 Sitzungen bei einer Langzeittherapie) mit der gemeinsamen Erarbeitung eines individuellen Störungsmodells und der Psychoedukation zu ihrer Diagnose. Das Ziel hierbei ist, dass sie die Auslöser ihrer Erkrankung ebenso erkennen, wie die Faktoren, die diese aufrechterhalten.<br>Die Kosten für die Therapie übernimmt bei gesetzlich Versicherten nach positivem Bescheid die Krankenkasse. Privatversicherte nehmen bitte zu Beginn der geplanten Therapie Kontakt mit ihrer privaten Krankenversicherung auf und besprechen die Kostenübernahme.</p>
    </section>

    <section class="phase phase-3">
      <h2 class="phase-title">3. Rückfallprophylaxe</h2>
      <p>Zu gegebenem Zeitpunkt und mit erreichtem Fortschritt werden die wöchentlichen Therapiesitzungen auf einen zweiwöchigen Rhythmus umgestellt, so dass sie selbständig Erfahrungen in der Anwendung des Erlernten sammeln können und gleichzeitig weiterhin therapeutische Unterstützung erfahren.</p>
    </section>
  </main>

  <section class="cta-band">
    <p class="cta-text">Erfahren Sie etwas über meine Person</p>
    <a href="#" class="cta-button">Mehr erfahren</a>
  </section>

  <footer class="site-footer">
    <div class="footer-col contact">
      <h3 class="footer-heading">Psychotherapeutische Praxis Hollmann</h3>
      <div class="contact-row row-address">
        <svg width="14" height="20" viewBox="0 0 14 20"><path d="M7 1a6 6 0 0 0-6 6c0 4.5 6 12 6 12s6-7.5 6-12a6 6 0 0 0-6-6z" fill="none" stroke="#fff" stroke-width="1.4"/><circle cx="7" cy="7" r="2.2" fill="none" stroke="#fff" stroke-width="1.2"/></svg>
        <span>Lindenhofweg 12<br>60439 Frankfurt/Main</span>
      </div>
      <div class="contact-row row-phone">
        <svg width="15" height="15" viewBox="0 0 15 15"><path d="M1 4c0-2 13-2 13 0v1.5h-3V4H4v1.5H1z" fill="#fff"/><g fill="#fff"><circle cx="5" cy="8" r=".9"/><circle cx="7.5" cy="8" r=".9"/><circle cx="10" cy="8" r=".9"/><circle cx="5" cy="10.5" r=".9"/><circle cx="7.5" cy="10.5" r=".9"/><circle cx="10" cy="10.5" r=".9"/><circle cx="5" cy="13" r=".9"/><circle cx="7.5" cy="13" r=".9"/><circle cx="10" cy="13" r=".9"/></g></svg>
        <span>0176 / 248 31 57</span>
      </div>
      <div class="contact-row row-mail">
        <svg width="14" height="14" viewBox="0 0 14 14"><path d="M13 1L1 6l5 2 2 5z M13 1L6 8" fill="none" stroke="#fff" stroke-width="1.1" stroke-linejoin="round"/></svg>
        <span>hollmann-therapie@postfach-mail.de</span>
      </div>
    </div>

    <div class="footer-col notes">
      <h3 class="footer-heading h-note">Hinweis</h3>
      <p class="footer-text">Aufgrund der&nbsp; Coronavirus /SARS-CoV-2- Krise<br>biete ich zertifizierte Videosprechstunden an!</p>
      <h3 class="footer-heading h-phone">Telefonische Erreichbarkeit</h3>
      <p class="footer-text">Montags, dienstags, Mittwochs &amp; Donnerstags<br>von 13:00 bis 13:30 Uhr</p>
    </div>
  </footer>
</body>
</html>
```